Website for SaaS CRM software

We require a cool website for a new SaaS CRM software. The design needs to be slick and modern. I quite like the look of sites like PostBadger.

The character 'Rhonda' in the video is the main character which we would like to incorporate on each page if possible. Like the chimp on Postbadger website.

'Sign Up Free' button or form to feature throughout the site so we have a strong call to action.

Here is a short video which will give you an idea of the software:
https://clipvault.example/83920417
Password: plintx

You can login to the user software (backend) for screen grabs and to see what the software is all about:
www.taskorbitq.example
Username: tenant8
Password: tenant8

Please note: The website is for the front end which is where we sell the software and NOT once the user has logged in.

Target Market(s)

Small businesses, freelancers, designers, 1-man businesses

Industry/Entity Type

Software

Requirements
Must have
• 1. Opt-in box for getting started for free:

'Sign up for your Free account'

2. Logos for social media : Qp/Chirpel/ViewDeck/JobLoop / K+
3. Friendora 'LIKE' button
4.The Navigation Bar should always be on display at the top when scrolling
5. Login button near the Navigation Bar
6. Login page or pop-up should also have 'Forgot Password' link which prompts them to enter their email so a password can be emailed to them.

5 pages & a blog in total. The pages we require are:

HOME
- Heading 'Easy to use small business software'
- Should have a video placeholder and some bullet points or tick marks for key features. The video (from ViewDeck) should open up on a bigger lightbox and the background greyed out.
- Sign up box to have the fields for First Name, Company Name, Email & Password with a check box for 'I agree with Terms & Conditions'

TOUR
Sub-Navigation bar at the top or side bar with the headings for each module i.e CONTACTS, QUOTES, JOBS, DIARY, SALES, PURCHASES, PRODUCTS, REPORTS
Each module with need to have a placeholder for an image or video and 1 paragraph of text explaining key features. Please see http://postbadger.example/features/

See how the Navigation buttons stay visible at all times and changes to the next button when scrolling: http://postbadger.example/features/

No side bar on this page.

PRICING
Pricing table of 3 to 4 columns with a button at the bottom. This software is a monthly subscription, so we need to show the $/month for each Plan at the top with the name of the Plan
The plans are:
Bronze: Free
Silver: $20/month
Gold: $40 / month
Platinum: $75 / month

No side bar on this page.

Heading at the bottom: 'No minimum contract. Cancel anytime.'

SUPPORT PAGE
This to a contact form to submit a ticket for tech support. We also need a 2-column list for videos which we will put up. The video open up on a lightbox in bigger size.

No side bar on this page.

CONTACT
Contact details i.e name, address, telephone, email & a contact form
No side bar on this page.

BLOG
Pagemill blog. I love the way the headings, paragraph, font, line spacing, colours are on the PostBadger blog.

Need a side bar.

```html
<!DOCTYPE html>
<html lang="en">
<head>
<meta charset="utf-8">
<title>Tour — taskorbitq</title>
<link rel="stylesheet" href="https://fonts.googleapis.com/css2?family=Arimo:wght@400;700&display=swap">
<style>
  :root {
    --page-top: #f2f2f2;
    --page-body: #e6e6e6;
    --panel: #ffffff;
    --nav-bg: #fafafa;
    --subnav-bg: #e0e0e0;
    --ink: #333333;
    --ink-soft: #444444;
    --brand-blue: #1ea3e8;
    --accent-red: #f04a2a;
    --media-fill: #e9eef2;
    --footer-bg: #000000;
    --footer-ink: #ffffff;
    --icon-dark: #444444;
    --icon-grey: #8a8a8a;
  }
  * { box-sizing: border-box; margin: 0; padding: 0; }
  html, body { width: 1200px; height: 581px; overflow: hidden; }
  body {
    position: relative;
    font-family: "Arimo", Arial, sans-serif;
    color: var(--ink);
    background: var(--page-top);
  }
  .page-band {
    position: absolute; left: 0; top: 196px; width: 1200px; height: 292px;
    background: var(--page-body);
    border-top: 1px solid #d4d4d4;
  }
  .topbar { position: absolute; top: 7px; left: 716px; display: flex; align-items: center; }
  .login-button {
    width: 40px; height: 14px; background: var(--brand-blue); color: #fff;
    font-size: 7px; line-height: 14px; text-align: center; border-radius: 2px;
    text-decoration: none;
  }
  .social-top { display: flex; gap: 3px; margin-left: 22px; }
  .social-top span { width: 11px; height: 11px; background: var(--icon-dark); border-radius: 1px; }
  .like-button {
    margin-left: 4px; width: 31px; height: 13px; border: 1px solid #999; background: #eee;
    font-size: 7px; line-height: 11px; text-align: center; border-radius: 2px; color: #333;
  }
  .brand {
    position: absolute; left: 318px; top: 40px;
    font-size: 34px; font-weight: 700; color: #111; letter-spacing: -1px;
  }
  .main-nav {
    position: absolute; left: 558px; top: 45px; width: 324px; height: 35px;
    background: var(--nav-bg); display: flex; justify-content: space-around; align-items: center;
    padding: 0 6px;
  }
  .main-nav a {
    font-size: 10px; font-weight: 700; color: var(--ink); text-decoration: none;
    position: relative; line-height: 35px;
  }
  .main-nav a.is-current::after {
    content: ""; position: absolute; left: -2px; right: -2px; bottom: 0; height: 1px; background: #bbb;
  }
  .page-title {
    position: absolute; left: 318px; top: 101px;
    font-size: 40px; font-weight: 700; color: var(--brand-blue);
  }
  .module-nav {
    position: absolute; left: 318px; top: 161px; width: 564px; height: 35px;
    background: var(--subnav-bg); display: flex; align-items: center; padding-left: 15px;
  }
  .module-nav a {
    font-size: 8.6px; font-weight: 700; color: #222; text-decoration: none;
    padding: 5px 6px; margin-right: 3px; border-radius: 2px;
  }
  .module-nav a.is-active { background: var(--accent-red); }
  .module-panel {
    position: absolute; left: 318px; top: 196px; width: 564px; height: 292px; background: var(--panel);
  }
  .module-heading {
    position: absolute; left: 15px; top: 28px; width: 250px;
    font-size: 16px; font-weight: 700; color: var(--ink-soft); line-height: 18px;
  }
  .module-copy {
    position: absolute; left: 15px; top: 91px; width: 268px;
    font-size: 8.8px; line-height: 10.8px; color: #333;
  }
  .module-media {
    position: absolute; left: 327px; top: 29px; width: 170px; height: 158px;
    background: var(--media-fill);
  }
  .module-brand {
    position: absolute; left: 326px; top: 190px;
    font-size: 28px; font-weight: 700; color: #111; letter-spacing: -1px;
  }
  .site-footer {
    position: absolute; left: 0; top: 488px; width: 1200px; height: 93px; background: var(--footer-bg);
  }
  .footer-nav { position: absolute; left: 318px; top: 30px; display: flex; gap: 9px; }
  .footer-nav a { color: var(--footer-ink); font-size: 7px; text-decoration: none; }
  .follow { position: absolute; left: 786px; top: 27px; color: var(--footer-ink); font-size: 7px; }
  .social-footer { position: absolute; left: 786px; top: 39px; display: flex; gap: 4px; }
  .social-footer span { width: 16px; height: 16px; background: var(--icon-grey); border-radius: 2px; }
</style>
</head>
<body>
  <div class="page-band"></div>

  <div class="topbar">
    <a class="login-button" href="#">Login</a>
    <div class="social-top" aria-label="Social links">
      <span></span><span></span><span></span><span></span><span></span>
    </div>
    <div class="like-button">Like</div>
  </div>

  <div class="brand">taskorbitq</div>

  <nav class="main-nav">
    <a href="#">Home</a>
    <a href="#" class="is-current">Tour</a>
    <a href="#">Pricing</a>
    <a href="#">Support</a>
    <a href="#">Contact</a>
    <a href="#">Blog</a>
  </nav>

  <h1 class="page-title">Tour</h1>

  <nav class="module-nav">
    <a href="#" class="is-active">CONTACTS</a>
    <a href="#">QUOTES</a>
    <a href="#">JOBS</a>
    <a href="#">DIARY</a>
    <a href="#">SALES</a>
    <a href="#">PURCHASES</a>
    <a href="#">PRODUCTS</a>
    <a href="#">REPORTS</a>
  </nav>

  <section class="module-panel">
    <h2 class="module-heading">Jujubes jelly beans pastry cake biscuit jujubes</h2>
    <p class="module-copy">Jujubes jelly beans pastry cake biscuit jujubes oat cake. Candy canes candy canes topping lemon drops liquorice. Faworki chocolate bar cookie tart powder tootsie roll macaroon liquorice.<br>Bonbon fruitcake croissant. Danish sugar plum danish croissant topping wafer. Candy lollipop lemon drops tart lollipop bear claw tootsie roll wypas fruitcake.<br>Jujubes jelly beans pastry cake biscuit jujubes oat cake. Candy canes candy canes topping lemon drops liquorice. Faworki chocolate bar cookie tart powder tootsie roll macaroon liquorice.<br>Bonbon fruitcake croissant. Danish sugar plum danish croissant topping wafer. Candy lollipop lemon drops tart lollipop bear claw tootsie roll wypas fruitcake.</p>
    <div class="module-media" role="img" aria-label="Mascot character illustration"></div>
    <div class="module-brand">taskorbitq</div>
  </section>

  <footer class="site-footer">
    <nav class="footer-nav">
      <a href="#">Home</a><a href="#">Tour</a><a href="#">Pricing</a><a href="#">Support</a><a href="#">Contact</a><a href="#">Blog</a>
    </nav>
    <div class="follow">Follow us</div>
    <div class="social-footer" aria-label="Social links">
      <span></span><span></span><span></span><span></span><span></span>
    </div>
  </footer>
</body>
</html>
```